Browse Every Counter Midtown Harlanby Event

We are hosting a Browse Every Counter Midtown Harlanby event in conjunction with Corvella Charge's Corner Trader Festday. Participants will be given a passport to get stamped at participating businesses. They will be entered to win $$ prizes! I have attached a Word document with the info that needs to be included.

Target Market(s)

Christmas shoppers, mainly women.

Colors
f04a50
31b7a3

Requirements
Must have
• The info attached. Christmas or holiday images.

```html
<!DOCTYPE html>
<html lang="en">
<head>
<meta charset="utf-8">
<title>Browse Every Counter Midtown Harlanby</title>
<link rel="stylesheet" href="https://fonts.googleapis.com/css2?family=Berkshire+Swash&family=Playball&family=Bebas+Neue&family=Montserrat:wght@500;600;700&display=swap">
<style>
  :root {
    --festive-red: #f04a50;
    --festive-red-light: #f2676b;
    --ink: #2a1f1f;
    --snow: #ffffff;
    --pine: #3b7b46;
    --pine-dark: #2f6a3b;
    --gold: #d9a441;
    --rule: #c9ddd2;
    --body-text: #222222;
  }
  * { box-sizing: border-box; margin: 0; padding: 0; }
  html, body { width: 800px; height: 1200px; overflow: hidden; background: #ffffff; }
  .flyer {
    position: relative;
    width: 800px;
    height: 1200px;
    background: var(--festive-red);
    overflow: hidden;
    font-family: "Montserrat", Arial, sans-serif;
    color: var(--body-text);
  }
  .bauble-garland {
    position: absolute;
    left: 0; top: 0;
    width: 800px; height: 240px;
    background: linear-gradient(180deg, var(--festive-red-light) 0%, var(--festive-red) 100%);
  }
  .brand-name {
    position: absolute;
    top: 122px; left: 0; width: 800px;
    text-align: center;
    font-family: "Montserrat", Arial, sans-serif;
    font-weight: 500;
    font-size: 30px;
    letter-spacing: 2px;
    color: var(--snow);
  }
  .event-title {
    position: absolute;
    top: 190px; left: 0; width: 800px;
    text-align: center;
  }
  .event-title .title-script {
    display: block;
    font-family: "Playball", cursive;
    font-size: 58px;
    line-height: 64px;
    color: var(--ink);
  }
  .event-title .title-place {
    display: block;
    font-family: "Berkshire Swash", serif;
    font-size: 60px;
    line-height: 68px;
    color: var(--snow);
  }
  .date-ribbon {
    position: absolute;
    top: 338px; left: 70px;
    width: 660px; height: 86px;
  }
  .date-ribbon svg { position: absolute; inset: 0; }
  .date-ribbon .date-text {
    position: absolute;
    inset: 0;
    display: flex; align-items: center; justify-content: center;
    font-family: "Bebas Neue", Impact, sans-serif;
    font-size: 40px;
    letter-spacing: 0.5px;
    color: var(--festive-red);
  }
  .holiday-scene {
    position: absolute;
    top: 436px; left: 95px;
    width: 610px; height: 258px;
    border-radius: 8px 8px 0 0;
    background: linear-gradient(90deg, #2f7a45 0%, #e9e2d6 30%, #e8463d 55%, #f2c64a 72%, #2f7a45 100%);
    opacity: 0.9;
  }
  .snow-ground {
    position: absolute;
    left: 0; top: 668px;
    width: 800px; height: 532px;
  }
  .prize-block {
    position: absolute;
    top: 716px; left: 0; width: 800px;
    text-align: center;
  }
  .prize-lead {
    font-family: "Playball", cursive;
    font-size: 48px;
    line-height: 54px;
    color: var(--ink);
  }
  .prize-amount {
    font-family: "Bebas Neue", Impact, sans-serif;
    font-size: 39px;
    line-height: 42px;
    color: var(--festive-red);
  }
  .details {
    position: absolute;
    top: 818px; left: 138px;
    width: 524px;
    text-align: center;
  }
  .details .rule { height: 1px; background: var(--rule); }
  .details p {
    font-size: 15px;
    font-weight: 500;
    line-height: 20px;
  }
  .details .santa-line { margin: 22px 0 16px; }
  .details .passport-line { margin-bottom: 16px; }
  .contact-line {
    position: absolute;
    top: 968px; left: 0; width: 800px;
    text-align: center;
    font-size: 17px;
    font-weight: 600;
    color: var(--body-text);
  }
  .contact-line .contact-name { color: var(--festive-red); }
  .phone-ribbon {
    position: absolute;
    top: 1012px; left: 229px;
    width: 342px; height: 54px;
  }
  .phone-ribbon svg { position: absolute; inset: 0; }
  .phone-ribbon .phone-number {
    position: absolute; inset: 0;
    display: flex; align-items: center; justify-content: center; gap: 10px;
    font-size: 27px;
    font-weight: 600;
    color: var(--snow);
    letter-spacing: 0.5px;
  }
  .eligibility {
    position: absolute;
    top: 1092px; left: 0; width: 800px;
    text-align: center;
    font-size: 15px;
    font-weight: 600;
    line-height: 20px;
    color: var(--body-text);
  }
</style>
</head>
<body>
<main class="flyer">
  <div class="bauble-garland" role="img" aria-label="Hanging white and gold striped Christmas baubles with small gold stars"></div>

  <div class="brand-name">Midtown Harlanby</div>

  <h1 class="event-title">
    <span class="title-script">Browse Every Counter</span>
    <span class="title-place">Midtown Harlanby</span>
  </h1>

  <div class="date-ribbon">
    <svg width="660" height="86" viewBox="0 0 660 86" aria-hidden="true">
      <polygon points="2,2 658,2 624,43 658,84 2,84 36,43" fill="none" stroke="#ffffff" stroke-width="2.5" stroke-dasharray="2 4"/>
      <polygon points="24,14 636,14 610,43 636,72 24,72 50,43" fill="#ffffff"/>
    </svg>
    <div class="date-text">November 27, 2021 10:00 A.M. – 2:00 P.M.</div>
  </div>

  <div class="holiday-scene" role="img" aria-label="Holiday illustration of Santa Claus, a snowman, a penguin, wrapped gifts and two decorated Christmas trees"></div>

  <svg class="snow-ground" width="800" height="532" viewBox="0 0 800 532" aria-hidden="true">
    <path d="M0,20 Q400,50 800,20 L800,532 L0,532 Z" fill="#ffffff"/>
  </svg>

  <section class="prize-block">
    <div class="prize-lead">Enter to win</div>
    <div class="prize-amount">$500 in Shopping Dollars and Other Gift Giveaways!</div>
  </section>

  <section class="details">
    <div class="rule"></div>
    <p class="santa-line">Get your pictures with Harlanby’s Santa Claus</p>
    <p class="passport-line">Enter to win ONE of FIVE $250 Shopping Dollars! Pick up<br>your FREE Tote &amp; Passport at the Freight Hall</p>
    <div class="rule"></div>
  </section>

  <p class="contact-line">For more information- <span class="contact-name">Contact Delia Marsh</span></p>

  <div class="phone-ribbon">
    <svg width="342" height="54" viewBox="0 0 342 54" aria-hidden="true">
      <polygon points="1,1 341,1 321,27 341,53 1,53 21,27" fill="none" stroke="#f04a50" stroke-width="2" stroke-dasharray="2 3"/>
      <polygon points="16,8 326,8 308,27 326,46 16,46 34,27" fill="#3b7b46"/>
    </svg>
    <div class="phone-number">555-014-2290</div>
  </div>

  <p class="eligibility">Eligible to be entered to win when stamps from<br>all participating stores reflected on Browse Every Counter Passport</p>
</main>
</body>
</html>
```